MAREK DOLVANE FOR CONGRESS DISTRICT 32

I need to create a campaign flyer for my congress campaign. I am running for congress in District 32 of Texas as a republican. I am a former Olympic athlete, world champion fencer, Army veteran, Counterintelligence officer (I catch spies).
I want just my first name MAREK in big letters at the top. I want it to say MAREK and below it Republican for Congress.
www.marekforcongress.example

Industry/Entity Type

Political

Colors
EB3D1F
EC4F4E
F09395
F8D3D4
FCEDEE

Requirements
Nice to have
• Would love a catchy title for the Flyer like "Spy Catcher", "Olympic Athlete" "World Champion Fencer" running for Congress in your District!

```html
<!DOCTYPE html>
<html lang="en">
<head>
<meta charset="utf-8">
<title>Marek Dolvane for Congress – Flyer</title>
<link rel="stylesheet" href="https://fonts.googleapis.com/css2?family=Archivo+Black&family=Roboto+Condensed:wght@300;400;700&family=Roboto:wght@500;900&display=swap">
<style>
  :root {
    --navy: #1f0c68;
    --navy-text: #2a1470;
    --red: #d91d13;
    --red-deep: #c8201c;
    --plum: #5a0f4f;
    --white: #ffffff;
    --ink: #111111;
    --page-bg: #f2f2f2;
    --photo-light: #f1eeec;
    --photo-warm: #d9a68e;
  }
  html, body {
    margin: 0;
    width: 1200px;
    height: 1200px;
    overflow: hidden;
    background: var(--page-bg);
  }
  .flyer {
    position: absolute;
    left: 180px;
    top: 52px;
    width: 840px;
    height: 1096px;
    background: var(--white);
  }
  .flyer svg { display: block; }
  .tagline { font-family: "Roboto Condensed", sans-serif; font-weight: 400; font-size: 29px; fill: var(--white); letter-spacing: 0.5px; }
  .candidate-first-name { font-family: "Archivo Black", sans-serif; font-size: 258px; fill: var(--white); }
  .office-line { font-family: "Roboto Condensed", sans-serif; font-weight: 300; font-size: 44px; fill: var(--white); }
  .quote-text { font-family: "Roboto Condensed", sans-serif; font-weight: 700; font-size: 27px; fill: var(--white); }
  .quote-mark { font-family: "Archivo Black", sans-serif; font-size: 40px; fill: var(--white); }
  .campaign-name { font-family: "Roboto Condensed", sans-serif; font-weight: 700; font-size: 36px; fill: var(--red-deep); }
  .campaign-district { font-family: "Roboto Condensed", sans-serif; font-weight: 700; font-size: 18px; fill: var(--navy-text); }
  .contact-email { font-family: "Roboto", sans-serif; font-weight: 500; font-size: 25px; fill: var(--navy-text); }
  .contact-web { font-family: "Roboto", sans-serif; font-weight: 500; font-size: 22px; fill: var(--navy-text); }
  .vote-label { font-family: "Roboto", sans-serif; font-weight: 900; font-size: 29px; fill: var(--ink); }
</style>
</head>
<body>
<div class="flyer">
  <svg width="840" height="1096" viewBox="0 0 840 1096" xmlns="http://www.w3.org/2000/svg">
    <defs>
      <linearGradient id="panelGradient" x1="0" y1="0" x2="1" y2="1">
        <stop offset="0.5" stop-color="var(--navy)"/>
        <stop offset="0.68" stop-color="var(--plum)"/>
        <stop offset="0.85" stop-color="var(--red)"/>
      </linearGradient>
      <linearGradient id="quoteGradient" x1="0" y1="0" x2="0.6" y2="1">
        <stop offset="0" stop-color="var(--plum)"/>
        <stop offset="0.45" stop-color="var(--red)"/>
      </linearGradient>
      <linearGradient id="photoGradient" x1="0" y1="0" x2="0" y2="1">
        <stop offset="0" stop-color="var(--photo-warm)"/>
        <stop offset="0.55" stop-color="var(--photo-light)"/>
      </linearGradient>
    </defs>

    <path class="header-panel" fill="url(#panelGradient)"
      d="M41 41 H799 V865 L692 854 L546 810 L466 780 L444 762 L422 740 L400 722 L356 707 L107 605 L100 597 L78 590 L41 586 Z"/>

    <text class="tagline" x="420" y="91" text-anchor="middle">VETERAN. OLYMPIAN. LEADER.</text>
    <text class="candidate-first-name" x="132" y="299" textLength="578" lengthAdjust="spacingAndGlyphs">MAREK</text>
    <text class="office-line" x="134" y="354" textLength="578" lengthAdjust="spacing">REPUBLICAN FOR CONGRESS</text>

    <rect class="candidate-photo" role="img" aria-label="Portrait photo of the candidate in a white shirt"
      x="478" y="365" width="321" height="505" rx="120" ry="120" fill="url(#photoGradient)"/>

    <rect class="quote-card" x="113" y="515" width="243" height="306" rx="14" fill="url(#quoteGradient)"/>
    <circle class="quote-badge" cx="234" cy="517" r="23" fill="var(--red)"/>
    <text class="quote-mark" x="234" y="537" text-anchor="middle">“</text>
    <text class="quote-text">
      <tspan x="125" y="578">I do have special</tspan>
      <tspan x="125" y="615">interests. America.</tspan>
      <tspan x="125" y="651">Americans. The</tspan>
      <tspan x="125" y="688">days of spending</tspan>
      <tspan x="125" y="724">absurd amounts of</tspan>
      <tspan x="125" y="761">money on foreign</tspan>
      <tspan x="125" y="798">interests are over.</tspan>
    </text>

    <text class="campaign-name" x="105" y="887" textLength="236" lengthAdjust="spacingAndGlyphs">MAREK DOLVANE</text>
    <text class="campaign-district" x="105" y="907" textLength="236" lengthAdjust="spacing">FOR CONGRESS TEXAS-32</text>
    <rect class="campaign-mark" x="352" y="868" width="28" height="28" fill="var(--navy)"/>

    <g class="icon-mail" transform="translate(104 951)">
      <rect x="0" y="0" width="18" height="13" rx="1.5" fill="var(--ink)"/>
      <path d="M1 1.5 L9 7.5 L17 1.5" fill="none" stroke="var(--white)" stroke-width="1.6"/>
    </g>
    <text class="contact-email" x="132" y="968">info@marekforcongress.example</text>

    <g class="icon-globe" transform="translate(113 991)" fill="none" stroke="var(--ink)" stroke-width="1.8">
      <circle r="9"/>
      <ellipse rx="4" ry="9"/>
      <line x1="-9" y1="0" x2="9" y2="0"/>
      <line x1="-8" y1="-4.5" x2="8" y2="-4.5"/>
      <line x1="-8" y1="4.5" x2="8" y2="4.5"/>
    </g>
    <text class="contact-web" x="134" y="999">www.marekforcongress.example</text>

    <circle class="vote-ring" cx="668" cy="947" r="30" fill="none" stroke="var(--red-deep)" stroke-width="4"/>
    <path class="vote-tick" d="M649 946 L663 960 L709 914 L664 952 Z" fill="var(--ink)"/>
    <text class="vote-label" x="668" y="1011" text-anchor="middle">VOTE</text>
  </svg>
</div>
</body>
</html>
```